Redesign for a start up airline technology. The website is trelunor.com.

I need a PowerPoint template that complements our website. I can provide our current template as a starting point.

```html
<!DOCTYPE html>
<html lang="en">
<head>
<meta charset="utf-8">
<title>Trelunor Presentation Template</title>
<link href="https://fonts.googleapis.com/css2?family=Montserrat:wght@400;500;600;800&display=swap" rel="stylesheet">
<style>
:root{
  --navy:#0a3a8c;
  --blue:#0b4aa2;
  --green:#3f9f45;
  --lime:#7dc242;
  --ink:#1c2a44;
  --grey:#5b5f66;
  --stage:#b9bbbf;
  --band:linear-gradient(90deg,#0a3d8f 0%,#0d58a0 45%,#3f9f45 100%);
  --photo:linear-gradient(90deg,#030f1e 0%,#123c6e 45%,#3e8f47 100%);
}
*{margin:0;padding:0;box-sizing:border-box}
html,body{width:756px;height:1200px;overflow:hidden}
body{background:var(--stage);font-family:"Montserrat",sans-serif;color:var(--ink);position:relative}
.top{position:absolute;left:0;top:0;width:756px;height:460px;background:linear-gradient(180deg,#dfe1e6,#c4c6ca)}
.brand{font-family:"Montserrat",sans-serif;font-weight:800;color:var(--blue);display:flex;align-items:center;gap:.25em;letter-spacing:.02em;white-space:nowrap}
.brand::before{content:"";width:.55em;height:.55em;border-radius:50%;background:var(--lime)}
.brand.light{color:#fff}
.brand.hero-mark{position:absolute;right:48px;top:42px;font-size:34px}
.hero{position:absolute;left:128px;top:92px;width:500px;height:300px;background:#fff;box-shadow:0 6px 18px rgba(0,0,0,.25)}
.hero .art{position:absolute;left:0;top:0;width:500px;height:281px;background:var(--photo)}
.hero .brand{position:absolute;left:40px;top:40px;font-size:22px;color:#fff}
.hero h1{position:absolute;left:40px;top:100px;font-size:34px;line-height:1.05;font-weight:800;color:#fff}
.hero .sub{position:absolute;left:40px;top:184px;font-size:13px;color:#fff}
.hero .date{position:absolute;left:40px;top:226px;font-size:8px;color:#fff}
.hero .foot{position:absolute;left:0;top:281px;width:100%;text-align:center;font-size:5px;line-height:19px;color:#555}

.slide{position:absolute;width:236px;height:133px;background:#fff;overflow:hidden}
.c1{left:13px}.c2{left:261px}.c3{left:508px}.c4{left:136px}.c5{left:384px}
.r1{top:473px}.r2{top:618px}.r3{top:762px}.r4{top:906px}.r5{top:1051px}
.art{display:block}
.cover-band{position:absolute;left:0;top:29px;width:236px;height:94px;background:var(--band)}
.cover-band.blue{background:linear-gradient(90deg,#0a3d8f,#0d5aa0 60%,#0f79b6)}
.slide .cover-brand{position:absolute;left:17px;top:10px;font-size:12px}
.title{position:absolute;left:24px;font-weight:800;color:#fff;font-size:13.5px;line-height:1.08}
.subt{position:absolute;left:24px;font-size:6px;color:#fff}
.dt{position:absolute;left:24px;font-size:3.2px;color:#fff}
.copy{position:absolute;left:0;bottom:0;width:100%;height:10px;background:#fff;text-align:center;font-size:3px;line-height:10px;color:#777}
.h{position:absolute;font-weight:800;color:var(--blue);font-size:8px;white-space:nowrap}
.h.light{color:#fff}
.rule{position:absolute;width:18px;height:2px;border-radius:2px;background:linear-gradient(90deg,var(--green),#cfe8c6)}
.mini-brand{position:absolute;right:8px;top:11px;font-size:6px}
.tx{position:absolute;font-size:3.2px;line-height:1.25;color:var(--grey)}
.tx.light{color:#fff}
.tx p{margin-bottom:1.6px}
.ft{position:absolute;left:6px;bottom:3px;font-size:2.8px;color:#444}
.fr{position:absolute;right:6px;bottom:2px;font-size:2.8px;color:#666;display:flex;align-items:center;gap:3px}
.pg{display:inline-block;width:5px;height:5px;border-radius:1px;background:var(--blue)}
.person{position:absolute;top:32px;width:31px;height:43px;border:1.5px solid #fff;background:linear-gradient(180deg,#bfc2c7,#6e7279)}
.pname{position:absolute;top:78px;width:44px;text-align:center;font-size:3.6px;font-weight:800;color:var(--blue)}
.prole{position:absolute;top:83px;width:44px;text-align:center;font-size:2.6px;color:var(--green)}
.pbio{position:absolute;top:88px;width:40px;text-align:center;font-size:2.5px;line-height:1.25;color:var(--grey)}
.col-h{position:absolute;font-size:4.5px;font-weight:800;color:var(--blue)}
.bul{position:absolute;font-size:2.8px;line-height:1.25;color:var(--grey);list-style:none}
.bul li{padding-left:3px;position:relative;margin-bottom:1px}
.bul li::before{content:"";position:absolute;left:0;top:1px;width:1.2px;height:1.2px;border-radius:50%;background:var(--green)}
.contact{position:absolute;left:26px;color:#fff;font-size:3.6px}
.contact .lab{font-weight:800;font-size:4.2px;margin-bottom:4px}
.contact .row{display:flex;align-items:center;gap:3px;margin-bottom:3px}
.contact svg{width:5px;height:5px}
</style>
</head>
<body>

<section class="top">
  <div class="brand hero-mark">Trelunor</div>
  <div class="hero">
    <div class="art" role="img" aria-label="Photo of an aircraft landing gear on a runway under a blue to green tint"></div>
    <div class="brand">Trelunor</div>
    <h1>Presentation<br>Title Goes Here</h1>
    <div class="sub">Subtitle of Presentation Goes Here</div>
    <div class="date">Wednesday, May 29, 2024</div>
    <div class="foot">© Trelunor, LLC. All Rights Reserved.</div>
  </div>
</section>

<!-- Row 1: covers -->
<div class="slide c1 r1">
  <div class="art" role="img" aria-label="Photo of aircraft landing gear with a dark blue to green tint" style="position:absolute;inset:0 0 10px 0;background:var(--photo)"></div>
  <div class="brand light" style="position:absolute;left:24px;top:18px;font-size:9px">Trelunor</div>
  <div class="title" style="top:49px">Presentation<br>Title Goes Here</div>
  <div class="subt" style="top:81px">Subtitle of Presentation Goes Here</div>
  <div class="dt" style="top:99px">Wednesday, May 29, 2024</div>
  <div class="copy">© Trelunor, LLC. All Rights Reserved.</div>
</div>
<div class="slide c2 r1">
  <div class="brand cover-brand">Trelunor</div>
  <div class="cover-band"></div>
  <div class="title" style="top:49px">Presentation<br>Title Goes Here</div>
  <div class="subt" style="top:81px">Subtitle of Presentation Goes Here</div>
  <div class="dt" style="top:99px">Wednesday, May 29, 2024</div>
  <div class="copy">© Trelunor, LLC. All Rights Reserved.</div>
</div>
<div class="slide c3 r1">
  <div class="brand cover-brand">Trelunor</div>
  <div class="cover-band blue"></div>
  <div class="title" style="top:49px">Presentation<br>Title Goes Here</div>
  <div class="subt" style="top:81px">Subtitle of Presentation Goes Here</div>
  <div class="dt" style="top:99px">Wednesday, May 29, 2024</div>
  <div class="copy">© Trelunor, LLC. All Rights Reserved.</div>
</div>

<!-- Row 2 -->
<div class="slide c1 r2">
  <div class="art" role="img" aria-label="Black and white close-up photo of an aircraft wing and engine" style="position:absolute;left:148px;top:0;width:88px;height:133px;background:linear-gradient(160deg,#e6e6e6,#6b6b6b 60%,#2b2b2b)"></div>
  <div class="brand mini-brand">Trelunor</div>
  <div class="h" style="left:21px;top:20px">Who We Are</div>
  <div class="rule" style="left:21px;top:31px"></div>
  <div class="tx" style="left:21px;top:38px;width:120px">Trelunor is an aerospace technology company building onboard weight and balance measurement for every flight.</div>
  <div style="position:absolute;left:0;top:64px;width:194px;height:43px;background:var(--band)"></div>
  <div class="tx light" style="left:21px;top:72px;width:70px">With many design and process patents, Trelunor brings engineering and certification expertise to aviation.</div>
  <div class="tx light" style="left:100px;top:72px;width:70px">Our leadership team holds decades of airline experience and delegated engineering authority.</div>
  <div class="ft">Confidential and Proprietary</div>
  <div class="fr" style="color:#eee">© Trelunor, LLC. All Rights Reserved. <span class="pg"></span></div>
</div>

<div class="slide c2 r2">
  <div class="h" style="left:13px;top:10px">The LDMS</div>
  <div class="rule" style="left:13px;top:21px"></div>
  <div class="brand mini-brand">Trelunor</div>
  <div class="art" role="img" aria-label="Technical drawing of a landing gear strut with sensors" style="position:absolute;left:14px;top:33px;width:63px;height:80px;background:linear-gradient(160deg,#0b1626,#05080f)"></div>
  <div class="tx" style="left:82px;top:36px;width:72px;text-align:center"><p>The Load Data Monitoring System is an onboard system that calculates aircraft weight and center of gravity for each flight.</p><p>Advanced sensors create efficiencies and flag maintenance issues early.</p></div>
  <div class="art" role="img" aria-label="Technical drawing of an aircraft seen from above with weight readings" style="position:absolute;left:160px;top:33px;width:63px;height:80px;background:linear-gradient(160deg,#0b1626,#05080f)"></div>
  <div class="ft">Confidential and Proprietary</div>
  <div class="fr">© Trelunor, LLC. All Rights Reserved. <span class="pg"></span></div>
</div>

<div class="slide c3 r2">
  <div style="position:absolute;left:0;top:0;width:236px;height:62px;background:var(--band)"></div>
  <div class="h light" style="left:13px;top:10px">Trelunor Leadership</div>
  <div class="rule" style="left:13px;top:21px"></div>
  <div class="brand light mini-brand">Trelunor</div>
  <div class="person" role="img" aria-label="Portrait of team member" style="left:15px"></div>
  <div class="person" role="img" aria-label="Portrait of team member" style="left:59px"></div>
  <div class="person" role="img" aria-label="Portrait of team member" style="left:103px"></div>
  <div class="person" role="img" aria-label="Portrait of team member" style="left:147px"></div>
  <div class="person" role="img" aria-label="Portrait of team member" style="left:190px"></div>
  <div class="pname" style="left:8px">Dale Morrow</div><div class="prole" style="left:8px">Founder and Senior Technical Fellow</div><div class="pbio" style="left:10px;top:91px">Leads product strategy and flight data systems.</div>
  <div class="pname" style="left:52px">Owen Hartley</div><div class="prole" style="left:52px">CEO</div><div class="pbio" style="left:54px">Leads product strategy and flight data systems.</div>
  <div class="pname" style="left:96px">Glen Pruitt</div><div class="prole" style="left:96px">Chief Operating Officer</div><div class="pbio" style="left:98px">Leads product strategy and flight data systems.</div>
  <div class="pname" style="left:140px">Ravi Menon</div><div class="prole" style="left:140px">CIO</div><div class="pbio" style="left:142px">Leads product strategy and flight data systems.</div>
  <div class="pname" style="left:184px">Neil Ashcroft</div><div class="prole" style="left:184px">Head of Engineering</div><div class="pbio" style="left:186px">Leads product strategy and flight data systems.</div>
  <div class="ft">Confidential and Proprietary</div>
  <div class="fr">© Trelunor, LLC. All Rights Reserved. <span class="pg"></span></div>
</div>

<!-- Row 3 -->
<div class="slide c1 r3">
  <div style="position:absolute;left:0;top:0;width:236px;height:52px;background:var(--band)"></div>
  <div class="h light" style="left:13px;top:10px">Commercial Aviation</div>
  <div class="rule" style="left:13px;top:21px"></div>
  <div class="brand light mini-brand">Trelunor</div>
  <div class="tx light" style="left:13px;top:27px;width:210px">An innovative approach to weight and balance planning turns estimates into actuals, optimizing load planning and reducing fuel burn.</div>
  <div class="art" role="img" aria-label="Black and white photo of a passenger cabin" style="position:absolute;left:13px;top:46px;width:103px;height:30px;background:linear-gradient(180deg,#d9d9d9,#7a7a7a)"></div>
  <div class="art" role="img" aria-label="Black and white photo of a cargo jet on the apron" style="position:absolute;left:121px;top:46px;width:103px;height:30px;background:linear-gradient(180deg,#8f8f8f,#3a3a3a)"></div>
  <div class="col-h" style="left:15px;top:81px">Passenger Airlines</div>
  <div class="col-h" style="left:122px;top:81px">Cargo</div>
  <ul class="bul" style="left:15px;top:88px;width:100px"><li>Better weight and balance data creates a more efficient load plan.</li><li>Consistent load plans improve fuel efficiency through reduced drag.</li><li>Data-driven insights provide quicker gate turn times for aircraft.</li></ul>
  <ul class="bul" style="left:122px;top:88px;width:100px"><li>Validated weight and center of gravity data provides actionable information.</li><li>Optimized center of gravity creates fuel efficiencies and savings.</li><li>Highlight efficiencies during loading and lower operational costs.</li></ul>
  <div class="ft">Confidential and Proprietary</div>
  <div class="fr">© Trelunor, LLC. All Rights Reserved. <span class="pg"></span></div>
</div>

<div class="slide c2 r3">
  <div class="art" role="img" aria-label="Photo of an aircraft flying between tall buildings seen from below" style="position:absolute;left:10px;top:0;width:90px;height:112px;background:linear-gradient(90deg,#3a3a3a,#dfe3e8 45%,#dfe3e8 60%,#3a3a3a)"></div>
  <div class="brand mini-brand">Trelunor</div>
  <div class="h" style="left:107px;top:40px">Regional and Business</div>
  <div class="rule" style="left:107px;top:51px"></div>
  <div class="tx" style="left:107px;top:63px;width:120px"><p>Accurate weight and loading data provides actionable information to get the most performance from your aircraft.</p><p>An optimized center of gravity creates fuel efficiencies which can translate into increased payload and range.</p><p>This data can also create efficiencies during the loading process, lowering operational costs and providing an increase return on investment.</p></div>
  <div class="ft">Confidential and Proprietary</div>
  <div class="fr">© Trelunor, LLC. All Rights Reserved. <span class="pg"></span></div>
</div>

<div class="slide c3 r3">
  <div class="h" style="left:13px;top:10px">Military</div>
  <div class="rule" style="left:13px;top:21px"></div>
  <div class="brand mini-brand">Trelunor</div>
  <div class="art" role="img" aria-label="Photo of a military turboprop aircraft flying at sunset" style="position:absolute;left:0;top:30px;width:236px;height:49px;background:linear-gradient(180deg,#3b2a22,#c9641f 55%,#f0a040)"></div>
  <div class="tx" style="left:13px;top:85px;width:212px"><p>Mission ready military aircraft are critical for success – humanitarian or war-fighting initiatives.</p><p>A data-driven plan for efficient loading optimizing the center of gravity and leads to shortened time on the ground, reduced fuel burn and increased time over target.</p><p>The Load Data Monitoring System continuously monitors aircraft landing gear system health, reducing unscheduled maintenance downtime.</p></div>
  <div class="ft">Confidential and Proprietary</div>
  <div class="fr">© Trelunor, LLC. All Rights Reserved. <span class="pg"></span></div>
</div>

<!-- Row 4 -->
<div class="slide c1 r4">
  <div class="h" style="left:13px;top:10px">Heading Goes Here</div>
  <div class="rule" style="left:13px;top:21px"></div>
  <div class="brand mini-brand">Trelunor</div>
  <div class="tx" style="left:13px;top:34px;width:212px"><p>Lorem ipsum dolor sit amet, consectetur adipiscing elit. Vivamus eu dui ex. Curabitur dapibus dignissim dui, in molestie metus feugiat sed. Praesent aliquet lorem ex, eu dapibus odio varius at. Duis eget tellus porta, consequat lacus vitae, venenatis dolor.</p><p>Nulla facilisi. In et sollicitudin lacus. Donec risus orci, gravida sit amet risus vehicula, aliquet pretium sapien. Nullam sit amet magna non ex bibendum mollis. Nunc vel neque eu augue dignissim congue ut vitae magna.</p><p>Phasellus eget commodo arcu. Nunc vitae semper dui. Integer venenatis, tellus sit amet interdum pretium, erat neque rhoncus turpis, a aliquam augue ligula eget erat. Nunc placerat, arcu nec mattis fermentum, nisi mauris convallis nunc.</p></div>
  <div class="ft">Confidential and Proprietary</div>
  <div class="fr">© Trelunor, LLC. All Rights Reserved. <span class="pg"></span></div>
</div>

<div class="slide c2 r4">
  <div class="art" role="img" aria-label="Photo of a hand launching a paper plane in a forest" style="position:absolute;left:118px;top:0;width:118px;height:133px;background:linear-gradient(90deg,#3a4a3a,#7d8b6c 50%,#2f3b2c)"></div>
  <div class="brand light mini-brand">Trelunor</div>
  <div class="h" style="left:17px;top:33px">Sustainability</div>
  <div class="rule" style="left:17px;top:44px"></div>
  <div style="position:absolute;left:0;top:50px;width:124px;height:17px;background:#555a5f"></div>
  <div class="tx light" style="left:17px;top:54px;width:90px">We are dedicated to helping our customers achieve zero carbon emissions by 2050.</div>
  <div class="tx" style="left:17px;top:79px;width:95px">Our next-generation technology focuses on improving fuel burn efficiency to significantly reduce CO2 emissions from aircraft, promote sustainability, streamline operations, and contribute to a greener aviation industry.</div>
  <div class="ft">Confidential and Proprietary</div>
  <div class="fr" style="color:#eee">© Trelunor, LLC. All Rights Reserved. <span class="pg"></span></div>
</div>

<div class="slide c3 r4">
  <div class="art" role="img" aria-label="Photo of aircraft landing gear under a blue to green tint" style="position:absolute;inset:0 0 10px 0;background:var(--photo)"></div>
  <div class="brand light" style="position:absolute;left:26px;top:20px;font-size:9px">Trelunor</div>
  <div class="title" style="left:26px;top:50px">Thank You!</div>
  <div class="contact" style="top:75px">
    <div class="lab">Contact Us</div>
    <div class="row"><svg viewBox="0 0 10 10"><path d="M2 1l2 2-1 1.2c.6 1.2 1.6 2.2 2.8 2.8L7 6l2 2-1.3 1.3C4.5 9 1 5.5.7 2.3z" fill="#fff"/></svg>555-0142-7781</div>
    <div class="row"><svg viewBox="0 0 10 10"><circle cx="5" cy="5" r="4" fill="none" stroke="#fff" stroke-width="1.2"/><circle cx="5" cy="5" r="1.5" fill="none" stroke="#fff" stroke-width="1.2"/></svg>info@trelunor.com</div>
    <div class="row"><svg viewBox="0 0 10 10"><circle cx="5" cy="5" r="4" fill="none" stroke="#fff" stroke-width="1"/><path d="M1 5h8M5 1c-2 2.5-2 5.5 0 8M5 1c2 2.5 2 5.5 0 8" fill="none" stroke="#fff" stroke-width=".8"/></svg>https://www.trelunor.com</div>
  </div>
  <div class="copy">© Trelunor, LLC. All Rights Reserved.</div>
</div>

<!-- Row 5 -->
<div class="slide c4 r5">
  <div class="brand cover-brand">Trelunor</div>
  <div class="cover-band"></div>
  <div class="title" style="left:26px;top:50px">Thank You!</div>
  <div class="contact" style="top:73px">
    <div class="lab">Contact Us</div>
    <div class="row"><svg viewBox="0 0 10 10"><path d="M2 1l2 2-1 1.2c.6 1.2 1.6 2.2 2.8 2.8L7 6l2 2-1.3 1.3C4.5 9 1 5.5.7 2.3z" fill="#fff"/></svg>555-0142-7781</div>
    <div class="row"><svg viewBox="0 0 10 10"><circle cx="5" cy="5" r="4" fill="none" stroke="#fff" stroke-width="1.2"/><circle cx="5" cy="5" r="1.5" fill="none" stroke="#fff" stroke-width="1.2"/></svg>info@trelunor.com</div>
    <div class="row"><svg viewBox="0 0 10 10"><circle cx="5" cy="5" r="4" fill="none" stroke="#fff" stroke-width="1"/><path d="M1 5h8M5 1c-2 2.5-2 5.5 0 8M5 1c2 2.5 2 5.5 0 8" fill="none" stroke="#fff" stroke-width=".8"/></svg>https://www.trelunor.com</div>
  </div>
  <div class="copy">© Trelunor, LLC. All Rights Reserved.</div>
</div>
<div class="slide c5 r5">
  <div class="brand cover-brand">Trelunor</div>
  <div class="cover-band blue"></div>
  <div class="title" style="left:26px;top:50px">Thank You!</div>
  <div class="contact" style="top:73px">
    <div class="lab">Contact Us</div>
    <div class="row"><svg viewBox="0 0 10 10"><path d="M2 1l2 2-1 1.2c.6 1.2 1.6 2.2 2.8 2.8L7 6l2 2-1.3 1.3C4.5 9 1 5.5.7 2.3z" fill="#fff"/></svg>555-0142-7781</div>
    <div class="row"><svg viewBox="0 0 10 10"><circle cx="5" cy="5" r="4" fill="none" stroke="#fff" stroke-width="1.2"/><circle cx="5" cy="5" r="1.5" fill="none" stroke="#fff" stroke-width="1.2"/></svg>info@trelunor.com</div>
    <div class="row"><svg viewBox="0 0 10 10"><circle cx="5" cy="5" r="4" fill="none" stroke="#fff" stroke-width="1"/><path d="M1 5h8M5 1c-2 2.5-2 5.5 0 8M5 1c2 2.5 2 5.5 0 8" fill="none" stroke="#fff" stroke-width=".8"/></svg>https://www.trelunor.com</div>
  </div>
  <div class="copy">© Trelunor, LLC. All Rights Reserved.</div>
</div>

</body>
</html>
```